Webdesign mit Software und IT Schwerpunkt
Zielgruppe
kleine und mittelständische Untrenehmen
Aufgabenstellung
Software-Service-Gesellschaft, spezialisiert auf Entwicklung und Betrieb von gewerblichen Webseiten mit selbstentwickeltem Service-Tool

```html
<!DOCTYPE html>
<html lang="de">
<head>
<meta charset="utf-8">
<title>NORDWERK – Webseiten pflegen mit dem LOTSE-Editor</title>
<link rel="stylesheet" href="https://fonts.googleapis.com/css2?family=Didact+Gothic&family=Open+Sans:wght@400;600;700&display=swap">
<style>
:root{
  --navy:#0c306c;
  --navy-mid:#34558c;
  --orange:#e8762b;
  --text:#3a3a3a;
  --head:#2e2e2e;
  --white:#ffffff;
  --line:#c4cfdf;
}
*{margin:0;padding:0;box-sizing:border-box}
html,body{width:1068px;height:1200px;overflow:hidden;background:var(--white)}
body{position:relative;font-family:"Didact Gothic",sans-serif;color:var(--text);font-size:12.5px;line-height:15.6px}
.abs{position:absolute}

.header{position:absolute;left:0;top:0;width:1068px;height:250px;
  background:linear-gradient(100deg,#ffffff 0%,#f3f5f9 30%,#9fb0cb 70%,#6f88ad 100%)}
.deco{position:absolute;left:0;top:0;width:1068px;height:1200px;pointer-events:none}
.toplinks{position:absolute;right:24px;top:16px;font-size:11.5px;color:var(--white);letter-spacing:.2px}
.toplinks span{margin:0 8px}
.logo-box{position:absolute;left:0;top:55px;width:308px;height:101px;background:var(--white);
  box-shadow:2px 3px 6px rgba(0,0,0,.35);display:flex;align-items:center;padding-left:24px;gap:12px}
.logo-mark{width:30px;height:30px;border-radius:50%;background:var(--orange)}
.logo-name{font-family:"Open Sans",sans-serif;font-weight:700;font-size:36px;color:var(--navy);letter-spacing:1px}

.claim{position:absolute;right:93px;text-align:right;color:var(--white);line-height:1.2}
.claim strong{font-family:"Open Sans",sans-serif;font-weight:700}
.claim-1{top:58px;font-size:27px}
.claim-2{top:88px;font-size:27px}
.claim-3{top:128px;font-size:27px}
.claim-3 strong{font-size:36px;font-weight:600}
.cta-top{position:absolute;left:714px;top:188px;width:261px;height:31px;background:var(--navy);
  border-left:12px solid var(--orange);color:var(--white);font-size:25px;text-align:center;line-height:31px}

.mainnav{position:absolute;left:0;top:250px;width:1068px;height:40px;background:var(--navy)}
.mainnav a{position:absolute;top:6px;color:var(--white);font-family:"Open Sans",sans-serif;font-weight:700;font-size:18.5px;line-height:26px;text-decoration:none}
.mainnav .active::after{content:"";position:absolute;left:-3px;right:-3px;bottom:-8px;height:5px;background:var(--orange)}
.subnav{position:absolute;left:0;top:290px;width:1068px;height:22px;background:var(--navy-mid)}
.subnav a{position:absolute;top:3px;color:var(--white);font-family:"Open Sans",sans-serif;font-weight:600;font-size:12px;text-decoration:none}

h2{font-family:"Open Sans",sans-serif;font-weight:700;font-size:18.5px;line-height:24px;color:var(--head)}
.lead{color:var(--orange);font-size:14px;line-height:18px;margin:11px 0 12px}
.lead strong{font-family:"Open Sans",sans-serif}
p{margin-bottom:12px}
p b{color:var(--navy);font-family:"Open Sans",sans-serif;font-weight:700}
.col-problem{left:72px;top:333px;width:300px}
.col-solution{left:438px;top:330px;width:312px}
.divider{left:72px;top:681px;width:678px;height:1px;background:var(--line)}

.teaser{top:720px;width:205px;line-height:16.5px}
.teaser h3{font-weight:400;font-size:15.5px;line-height:20px;color:var(--orange);margin-bottom:12px}
.teaser p{margin-bottom:10px}
.teaser-faq{left:72px}
.teaser-ref{left:323px}
.teaser-test{left:567px}
.vsep{top:720px;width:1px;height:145px;background:var(--line)}
.btn{display:block;background:var(--navy);border-left:9px solid var(--orange);color:var(--white);
  font-size:12.5px;height:20px;line-height:20px;padding-left:8px;width:185px;margin-bottom:11px;white-space:nowrap}
.btn b{font-family:"Open Sans",sans-serif}

.card{position:absolute;left:807px;width:205px;background:var(--white);border-radius:6px;
  box-shadow:1px 2px 6px rgba(0,0,0,.35);padding:16px 14px}
.card h4{font-weight:400;font-size:16px;color:var(--orange);line-height:20px}
.card h4 b{font-family:"Open Sans",sans-serif;font-weight:700}
.card .btn{width:182px;margin:0}
.card-login{top:333px;height:169px}
.card-login label{display:block;font-size:11px;margin-top:9px}
.card-login .field{width:132px;height:18px;border:1px solid #555;margin-top:2px}
.card-login .btn{margin-top:14px}
.card-opinion{top:520px;height:272px}
.bubble{position:relative;margin:6px -6px 0 -6px;height:170px}
.bubble svg{position:absolute;left:0;top:0}
.bubble-text{position:absolute;left:22px;top:20px;width:168px;text-align:right;color:var(--white);font-size:12px;line-height:15.5px}
.bubble-text i{display:block;font-style:italic;font-size:11px;margin-top:2px}
.card-opinion .btn{margin-top:4px}
.card-editor{top:810px;height:204px}
.screen{margin:12px -4px 8px;height:118px;border:1px solid #ccd;background:linear-gradient(180deg,#eef1f6 0%,#f7f8fa 40%,#e4e9f1 100%)}
.card-editor .btn{position:absolute;left:14px;top:164px}

.footer{position:absolute;left:0;top:1059px;width:1068px;height:141px;
  background:linear-gradient(100deg,#0c306c 0%,#23457e 45%,#8094b5 80%,#9fb0cb 100%)}
.fcol{position:absolute;top:1089px;color:var(--white);font-size:11px;line-height:1.2}
.fcol h5{font-family:"Open Sans",sans-serif;font-weight:700;font-size:11px;margin-bottom:17px}
.fcol .hl{font-family:"Open Sans",sans-serif;font-weight:700}
.flogo{position:absolute;left:847px;top:1102px;width:158px;height:56px;background:var(--white);
  display:flex;align-items:center;justify-content:center;gap:8px}
.flogo .logo-mark{width:16px;height:16px}
.flogo .logo-name{font-size:19px}
.copyright{position:absolute;left:866px;top:1161px;color:var(--white);font-size:11px;line-height:14px}
.copyright b{font-family:"Open Sans",sans-serif}
</style>
</head>
<body>

<div class="header"></div>

<svg class="deco" viewBox="0 0 1068 1200" aria-hidden="true">
  <g stroke="#ffffff" stroke-width="1.2" opacity=".85" fill="none">
    <line x1="1068" y1="0" x2="620" y2="1200"/>
    <line x1="960" y1="0" x2="1068" y2="60"/>
    <line x1="0" y1="1060" x2="120" y2="1200"/>
    <line x1="1068" y1="1040" x2="960" y2="1200"/>
  </g>
</svg>

<nav class="toplinks">Home<span>|</span>Impressum<span>|</span>Support<span>|</span>Sitemap</nav>

<div class="logo-box">
  <span class="logo-mark"></span>
  <span class="logo-name">NORDWERK</span>
</div>

<div class="claim claim-1">Ihre Webseiten <strong>pflegen</strong>?</div>
<div class="claim claim-2">So <strong>einfach</strong> wie E-Mail!</div>
<div class="claim claim-3">Mit dem <strong>LOTSE-Editor</strong></div>
<div class="cta-top">Jetzt testen</div>

<nav class="mainnav">
  <a class="active" style="left:75px">Start</a>
  <a style="left:135px">Produkte</a>
  <a style="left:237px">FAQ</a>
  <a style="left:297px">Referenzen</a>
  <a style="left:417px">Demos</a>
  <a style="left:504px">Preise</a>
</nav>
<nav class="subnav">
  <a style="left:72px">Unterpunkt1</a>
  <a style="left:165px">Unterpunkt2</a>
  <a style="left:250px">Unterpunkt3</a>
</nav>

<section class="abs col-problem">
  <h2>Sie haben ein Problem?</h2>
  <div class="lead">Sie sind unzufrieden mit Ihrer aktuellen Website - bezüglich Design, Technik oder Kosten?</div>
  <p><b>Unzureichendes Design</b>: Sie haben für Ihre Website noch kein ansprechendes Design oder das alte gefällt Ihnen nicht?</p>
  <p><b>Umständliche Aktualisierung</b>: Die Aktualisierung Ihrer Website ist kompliziert oder kann von Ihnen gar nicht durchgeführt werden?<br>Sie möchten keine kostenpflichtigen Updates installieren müssen?</p>
  <p><b>Unflexibel</b>: Sie möchten Ihre Website um Funktionen erweitern, wissen aber nicht wie?</p>
</section>

<section class="abs col-solution">
  <h2>Wir haben die Lösung für Sie!</h2>
  <div class="lead">So einfach wie Email - die Arbeit mit dem <strong>LOTSE-Editor!</strong></div>
  <p><b>Selber können</b>: Ihre Webseiten sind benutzerfreundlich von Ihnen änderbar. Sie brauchen nie Updates installieren, denn Sie nutzen immer automatisch die aktuellste Programmversion des <b>LOTSE-Editors</b>.</p>
  <p><b>Leichter Einstieg</b>: Wir übernehmen gerne Ihr existierendes Design zur Probe.</p>
  <p><b>Flexibel erweiterbar sein</b>: Sprechen Sie uns an. Von uns erstellte Seiten können günstig mit spezifischen Erweiterungen und Anwendungslogik versehen werden, inkl. Kontaktverwaltung, Statistiken, Weblog, Diashow oder Suchfunktion etc.</p>
</section>

<div class="abs divider"></div>

<section class="abs teaser teaser-faq">
  <h3>Fragen und Antworten</h3>
  <p>Die häufigsten Fragen und Antworten zu unseren Produkten finden Sie hier:</p>
  <span class="btn">Fragen zu <b>LOTSE-Editor</b></span>
</section>
<div class="abs vsep" style="left:289px"></div>
<section class="abs teaser teaser-ref">
  <h3>Unsere Referenzen</h3>
  <p>Sehen Sie sich unser System in der Praxis an. Umsetzungen unserer zufriedenen Kunden:</p>
  <span class="btn">Referenzen unserer Kunden</span>
</section>
<div class="abs vsep" style="left:535px"></div>
<section class="abs teaser teaser-test">
  <h3>Selbst testen</h3>
  <p>Testen Sie live unser System, sowohl das Frontend, als auch das Backend:</p>
  <span class="btn">Testseite live ansehen</span>
  <span class="btn">Testseite bearbeiten</span>
</section>

<aside class="card card-login">
  <h4>Login</h4>
  <label>Benutzername</label><div class="field"></div>
  <label>Passwort</label><div class="field"></div>
  <span class="btn">Einloggen</span>
</aside>

<aside class="card card-opinion">
  <h4>Meinungen unserer Kunden:</h4>
  <div class="bubble">
    <svg width="217" height="170" viewBox="0 0 217 150" preserveAspectRatio="none" aria-hidden="true">
      <defs><linearGradient id="bub" x1="0" y1="0" x2="1" y2="1">
        <stop offset="0" stop-color="#2b4f8a"/><stop offset="1" stop-color="#0c306c"/></linearGradient></defs>
      <path d="M40 6 C80 -4 180 -2 205 24 C222 48 216 104 192 124 C168 142 112 146 74 140 L36 150 L48 130 C12 114 2 82 5 52 C8 28 20 12 40 6 Z" fill="url(#bub)"/>
    </svg>
    <div class="bubble-text">„Jetzt geht das Aktualisieren meiner Seite deutlich leichter und effizineter von der Hand. Danke für dieses tolle Produkt!“<i>blauspecht.de</i></div>
  </div>
  <span class="btn">weiterlesen...</span>
</aside>

<aside class="card card-editor">
  <h4>Alles über den <b>LOTSE-Editor</b>:</h4>
  <div class="screen" role="img" aria-label="Bildschirmansicht des Editors beim Bearbeiten einer Webseite"></div>
  <span class="btn">Jetzt informieren</span>
</aside>

<footer class="footer"></footer>
<div class="fcol" style="left:104px"><h5>PRODUKTE</h5><div class="hl">LOTSE-Editor</div>Demo-Editor<br>Demo-Site</div>
<div class="fcol" style="left:260px"><h5>SERVICE</h5>FAQ<br>Kontakt<br>Sitemap</div>
<div class="fcol" style="left:417px"><h5>SONSTIGES</h5>AGBs<br>Disclaimer<br>Impressum</div>
<div class="flogo"><span class="logo-mark"></span><span class="logo-name">NORDWERK</span></div>
<div class="copyright">Copyright © 2009 by <b>nordwerk</b></div>

</body>
</html>
```